Brevin Electric Ltd

Looking for a single page website and Facebook page design. I am an electrical contractor based on Vancouver Island. I do service, custom homes, residential and commercial installations. My company just started out, so I don't have any pictures of installs yet. I have 25 years experience. I would like the colors to be my logo colors black and I have a black Torvik Ridgeman that will be my vehicle which I will have a wrap for.
Updates

I just posted the contest today, not sure why the deadline is the same day.

Went on vacation/holiday

Industry/Entity Type

Electrician

Requirements
Must have
• Services provided, About me section, quote section,
Nice to have
• I am not quite sure yet, I need to see some designs first .

```html
<!DOCTYPE html>
<html lang="en">
<head>
<meta charset="utf-8">
<title>Brevin Electric Ltd</title>
<link rel="stylesheet" href="https://fonts.googleapis.com/css2?family=Cinzel:wght@400;500&family=Open+Sans:ital,wght@0,400;0,600;0,700;0,800;1,700;1,800&display=swap">
<style>
  :root {
    --black: #000000;
    --ink: #1a1a1a;
    --yellow: #f2b61c;
    --white: #ffffff;
    --page: #eceef0;
    --muted: #333333;
  }
  * { margin: 0; padding: 0; box-sizing: border-box; }
  html, body { width: 1200px; height: 2848px; overflow: hidden; }
  body { background: var(--page); font-family: "Open Sans", Arial, sans-serif; position: relative; }
  a { text-decoration: none; }

  .site {
    position: absolute; left: 50px; top: 300px; width: 1100px; height: 2245px;
    background: var(--white); box-shadow: 8px 10px 22px rgba(0,0,0,.35); overflow: hidden;
  }

  /* header + hero */
  .hero { position: absolute; left: 0; top: 0; width: 1100px; height: 722px; background: var(--black); }
  .hero-photo {
    position: absolute; left: 0; top: 140px; width: 1100px; height: 582px;
    background:
      radial-gradient(ellipse 230px 170px at 560px 230px, #e0a450 0%, #b06a1f 35%, #4a2a0c 70%, transparent 100%),
      radial-gradient(ellipse 520px 150px at 520px 420px, #3a2e22 0%, #15110d 70%, #000 100%),
      #000;
  }
  .brand-name { position: absolute; left: 62px; top: 82px; color: var(--white); font-weight: 700; font-size: 14px; letter-spacing: .3px; white-space: nowrap; }
  .nav a { position: absolute; top: 84px; white-space: nowrap; font-family: "Cinzel", Georgia, serif; font-size: 15px; letter-spacing: 3px; color: var(--white); line-height: 22px; }
  .nav .active { background: var(--yellow); color: var(--ink); border-radius: 6px; padding: 0 6px; }
  .search { position: absolute; left: 891px; top: 84px; width: 186px; height: 22px; border: 1.5px solid #cfcfcf; display: flex; align-items: center; gap: 6px; padding-left: 6px; font-family: "Cinzel", Georgia, serif; font-size: 14px; letter-spacing: 3px; color: #ddd; }

  /* services */
  .band { position: absolute; left: 0; width: 1100px; height: 23px; display: flex; }
  .band span { flex: 0 0 auto; height: 100%; }
  .band .y { background: var(--yellow); }
  .band .b { background: var(--black); }
  .services { position: absolute; left: 0; top: 745px; width: 1100px; height: 369px; display: flex; }
  .service { width: 367px; height: 100%; text-align: center; padding-top: 14px; }
  .service:nth-child(2) { width: 366px; background: var(--yellow); }
  .service svg { width: 38px; height: 38px; }
  .service h2 { font-weight: 800; font-size: 24px; line-height: 30px; color: var(--ink); letter-spacing: .3px; }
  .service p { font-size: 11px; line-height: 12.8px; color: var(--ink); width: 270px; margin: 10px auto 0; }
  .service p + p { margin-top: 12px; }
  .pill { display: inline-block; background: var(--black); color: var(--yellow); font-weight: 700; font-style: italic; border-radius: 9px; border: 1.5px solid var(--yellow); }
  .service .pill { font-size: 11px; line-height: 15px; padding: 0 10px; margin-top: 10px; }

  /* why */
  .why { position: absolute; left: 0; top: 1137px; width: 1100px; height: 256px; text-align: center; }
  .why h2 { font-weight: 600; font-size: 45px; color: #2a2a2a; margin-top: 14px; line-height: 56px; }
  .why p { font-size: 11.8px; line-height: 13px; color: var(--muted); width: 930px; margin: 10px auto 0; }
  .why p + p { margin-top: 13px; }
  .cta { font-size: 19px; line-height: 26px; padding: 2px 18px; border-radius: 10px; margin-top: 22px; }

  /* about */
  .about { position: absolute; left: 0; top: 1393px; width: 550px; height: 459px; background: var(--yellow); padding: 40px 58px 0; }
  .about h2 { font-weight: 700; font-size: 42px; color: var(--ink); line-height: 50px; }
  .about p { font-size: 14px; line-height: 16.3px; color: var(--ink); margin-top: 14px; width: 430px; }
  .about p + p { margin-top: 18px; }
  .about .pill { font-size: 12.5px; padding: 1px 12px; margin-top: 26px; }
  .about-photo {
    position: absolute; left: 550px; top: 1393px; width: 550px; height: 459px;
    background: linear-gradient(110deg, #4a4c52 0%, #8a8d94 30%, #a36b3a 55%, #8d3a2a 75%, #b58a5a 100%);
  }

  /* quote band */
  .quote { position: absolute; left: 0; top: 1852px; width: 1100px; height: 220px; background: var(--black); text-align: center; padding-top: 26px; }
  .quote p { font-size: 11px; line-height: 12.5px; color: var(--white); width: 930px; margin: 0 auto; }
  .quote p + p { margin-top: 12px; }
  .quote .cta { background: var(--white); color: var(--ink); border-color: var(--white); margin-top: 20px; }

  /* footer */
  .footer { position: absolute; left: 0; top: 2072px; width: 1100px; height: 173px; background: var(--white); }
  .footer-brand { position: absolute; left: 0; top: 18px; width: 1100px; text-align: center; color: var(--ink); font-weight: 700; font-size: 14px; letter-spacing: .3px; }
  .footer-nav a { position: absolute; top: 58px; white-space: nowrap; font-family: "Cinzel", Georgia, serif; font-size: 18px; letter-spacing: 3.5px; color: #333; }
  .legal { position: absolute; left: 0; top: 102px; width: 1100px; text-align: center; font-family: "Cinzel", Georgia, serif; font-size: 13px; letter-spacing: 2.5px; color: #333; }
  .legal a { color: #333; margin: 0 20px; }
  .copyright { position: absolute; left: 0; top: 132px; width: 1100px; text-align: center; font-family: "Cinzel", Georgia, serif; font-size: 12.5px; letter-spacing: 2.5px; color: #333; }
</style>
</head>
<body>
<main class="site">

  <header class="hero">
    <div class="hero-photo" role="img" aria-label="Photo of a cracked glowing light bulb lying among broken glass on a dark surface"></div>
    <div class="brand-name">BREVIN ELECTRIC Ltd</div>
    <nav class="nav">
      <a class="active" href="#" style="left:287px">ABOUT US</a>
      <a href="#" style="left:427px">OPPORTUNITY</a>
      <a href="#" style="left:599px">WHY WHISKY</a>
      <a href="#" style="left:756px">CONTACT</a>
    </nav>
    <div class="search">
      <svg width="12" height="12" viewBox="0 0 12 12" fill="none" stroke="#ddd" stroke-width="1.6"><circle cx="5" cy="5" r="3.6"/><line x1="7.6" y1="7.6" x2="11" y2="11"/></svg>
      <span>Search</span>
    </div>
  </header>

  <div class="band" style="top:722px"><span class="y" style="width:367px"></span><span class="b" style="width:366px"></span><span class="y" style="width:367px"></span></div>

  <section class="services">
    <article class="service">
      <svg viewBox="0 0 40 40" aria-hidden="true"><path d="M20 4 3 19h5v17h24V19h5L20 4z" fill="#111"/><rect x="16" y="25" width="8" height="11" fill="#fff"/><rect x="12" y="19" width="5" height="4" fill="#fff"/><rect x="23" y="19" width="5" height="4" fill="#fff"/></svg>
      <h2>RESIDENTIAL</h2>
      <p>Lorem ipsum dolor sit amet, consectetuer adipiscing elit, sed diam nonummy nibh euismod tincidunt ut laoreet dolore magna aliquam erat volutpat. Ut wisi enim ad minim veniam, quis nostrud exerci tation ullamcorper suscipit lobortis nisl ut aliquip ex ea commodo consequat. Duis autem vel eum iriure dolor in hendrerit in vulputate velit esse molestie consequat, vel illum dolore eu feugiat nulla facilisis at vero eros et accumsan et iusto odio dignissim qui blandit praesent luptatum zzril delenit augue duis dolore te feugait nulla facilisi.</p>
      <p>dolor in hendrerit in vulputate velit esse molestie consequat, vel illum dolore eu feugiat nulla facilisis at vero eros et accumsan et iusto odio dignissim qui blandit praesent luptatum zzril delenit augue duis</p>
      <a class="pill" href="#">Learn More</a>
    </article>
    <article class="service">
      <svg viewBox="0 0 40 40" aria-hidden="true"><rect x="4" y="8" width="32" height="30" fill="#111"/><rect x="12" y="3" width="16" height="6" fill="#111"/><g fill="#f2b61c"><rect x="8" y="12" width="4" height="4"/><rect x="15" y="12" width="4" height="4"/><rect x="22" y="12" width="4" height="4"/><rect x="29" y="12" width="4" height="4"/><rect x="8" y="19" width="4" height="4"/><rect x="15" y="19" width="4" height="4"/><rect x="22" y="19" width="4" height="4"/><rect x="29" y="19" width="4" height="4"/><rect x="8" y="26" width="4" height="4"/><rect x="29" y="26" width="4" height="4"/><rect x="16" y="28" width="8" height="10"/></g></svg>
      <h2>COMMERCIAL</h2>
      <p>Lorem ipsum dolor sit amet, consectetuer adipiscing elit, sed diam nonummy nibh euismod tincidunt ut laoreet dolore magna aliquam erat volutpat. Ut wisi enim ad minim veniam, quis nostrud exerci tation ullamcorper suscipit lobortis nisl ut aliquip ex ea commodo consequat. Duis autem vel eum iriure dolor in hendrerit in vulputate velit esse molestie consequat, vel illum dolore eu feugiat nulla facilisis at vero eros et accumsan et iusto odio dignissim qui blandit praesent luptatum zzril delenit augue duis dolore te feugait nulla facilisi.</p>
      <p>dolor in hendrerit in vulputate velit esse molestie consequat, vel illum dolore eu feugiat nulla facilisis at vero eros et accumsan et iusto odio dignissim qui blandit praesent luptatum zzril delenit augue duis</p>
      <a class="pill" href="#">Learn More</a>
    </article>
    <article class="service">
      <svg viewBox="0 0 40 40" aria-hidden="true"><g fill="#111"><circle cx="20" cy="20" r="13"/><g transform="translate(20 20)"><rect x="-3" y="-18" width="6" height="8"/><rect x="-3" y="10" width="6" height="8"/><rect x="-18" y="-3" width="8" height="6"/><rect x="10" y="-3" width="8" height="6"/><g transform="rotate(45)"><rect x="-3" y="-18" width="6" height="8"/><rect x="-3" y="10" width="6" height="8"/><rect x="-18" y="-3" width="8" height="6"/><rect x="10" y="-3" width="8" height="6"/></g></g></g><circle cx="20" cy="20" r="8" fill="#fff"/><path d="M15 25l9-9m-1-2a3 3 0 1 0 4 4" stroke="#111" stroke-width="2.5" fill="none"/></svg>
      <h2>SERVICE</h2>
      <p>Lorem ipsum dolor sit amet, consectetuer adipiscing elit, sed diam nonummy nibh euismod tincidunt ut laoreet dolore magna aliquam erat volutpat. Ut wisi enim ad minim veniam, quis nostrud exerci tation ullamcorper suscipit lobortis nisl ut aliquip ex ea commodo consequat. Duis autem vel eum iriure dolor in hendrerit in vulputate velit esse molestie consequat, vel illum dolore eu feugiat nulla facilisis at vero eros et accumsan et iusto odio dignissim qui blandit praesent luptatum zzril delenit augue duis dolore te feugait nulla facilisi.</p>
      <p>dolor in hendrerit in vulputate velit esse molestie consequat, vel illum dolore eu feugiat nulla facilisis at vero eros et accumsan et iusto odio dignissim qui blandit praesent luptatum zzril delenit augue duis</p>
      <a class="pill" href="#">Learn More</a>
    </article>
  </section>

  <div class="band" style="top:1114px"><span class="y" style="width:367px"></span><span class="b" style="width:366px"></span><span class="y" style="width:367px"></span></div>

  <section class="why">
    <h2>Why Brevin Services</h2>
    <p>Lorem ipsum dolor sit amet, consectetuer adipiscing elit, sed diam nonummy nibh euismod tincidunt ut laoreet dolore magna aliquam erat volutpat. Ut wisi enim ad minim veniam, quis nostrud exerci tation ullamcorper suscipit lobortis nisl ut aliquip ex ea commodo consequat. Duis autem vel eum iriure dolor in hendrerit in vulputate velit esse molestie consequat, vel illum dolore eu feugiat nulla facilisis at vero eros et accumsan et iusto odio dignissim qui blandit praesent luptatum zzril delenit augue duis dolore te feugait nulla facilisi.</p>
    <p>dolor in hendrerit in vulputate velit esse molestie consequat, vel illum dolore eu feugiat nulla facilisis at vero eros et accumsan et iusto odio dignissim qui blandit praesent luptatum zzril delenit augue duis dolore te feugait nulla facilisi.</p>
    <a class="pill cta" href="#">SCHEDULE AN ESTIMATE</a>
  </section>

  <section class="about">
    <h2>About Us</h2>
    <p>Lorem ipsum dolor sit amet, consectetuer adipiscing elit, sed diam nonummy nibh euismod tincidunt ut laoreet dolore magna aliquam erat volutpat. Ut wisi enim ad minim veniam, quis nostrud exerci tation ullamcorper suscipit lobortis nisl ut aliquip ex ea commodo consequat. Duis autem vel eum iriure dolor in hendrerit in vulputate velit esse molestie consequat, vel illum dolore eu feugiat nulla facilisis at vero eros et accumsan et iusto odio dignissim qui blandit praesent luptatum zzril delenit augue duis dolore te feugait nulla facilisi.</p>
    <p>dolor in hendrerit in vulputate velit esse molestie consequat, vel illum dolore eu feugiat nulla facilisis at vero eros et accumsan et iusto odio dignissim qui blandit praesent luptatum zzril delenit augue duis dolore te feugait nulla facilisi.</p>
    <a class="pill" href="#">Learn More</a>
  </section>
  <div class="about-photo" role="img" aria-label="Photo of an electrician in a plaid shirt and tool apron stripping coloured wires with pliers"></div>

  <section class="quote">
    <p>Lorem ipsum dolor sit amet, consectetuer adipiscing elit, sed diam nonummy nibh euismod tincidunt ut laoreet dolore magna aliquam erat volutpat. Ut wisi enim ad minim veniam, quis nostrud exerci tation ullamcorper suscipit lobortis nisl ut aliquip ex ea commodo consequat. Duis autem vel eum iriure dolor in hendrerit in vulputate velit esse molestie consequat, vel illum dolore eu feugiat nulla facilisis at vero eros et accumsan et iusto odio dignissim qui blandit praesent luptatum zzril delenit augue duis dolore te feugait nulla facilisi.</p>
    <p>dolor in hendrerit in vulputate velit esse molestie consequat, vel illum dolore eu feugiat nulla facilisis at vero eros et accumsan et iusto odio dignissim qui blandit praesent luptatum zzril delenit augue duis dolore te feugait nulla facilisi.</p>
    <a class="pill cta" href="#">SCHEDULE AN ESTIMATE</a>
  </section>

  <footer class="footer">
    <div class="footer-brand">BREVIN ELECTRIC Ltd</div>
    <nav class="footer-nav">
      <a href="#" style="left:128px">HOME</a>
      <a href="#" style="left:248px">ABOUT US</a>
      <a href="#" style="left:416px">OPPORTUNITY</a>
      <a href="#" style="left:624px">WHY BREVIN</a>
      <a href="#" style="left:828px">CONTACT</a>
    </nav>
    <div class="legal"><a href="#">PRIVACY POLICY</a><a href="#">TERMS AND CONDITIONS</a></div>
    <div class="copyright">COPYRIGHT © 2022 LOREM IPSUM LTD - COMPANY REG NO:04718260</div>
  </footer>

</main>
</body>
</html>
```